Design a PowerPoint template for a consultancy organisation

I am after a Powerpoint template including three pages a title slide (that should have a title and subtitle), A title and content slide and a section header slide. I expect the company name and/or logo to be prominent and the colors to work well with the logo colors. I have included a copy of the logo

```html
<!DOCTYPE html>
<html lang="en">
<head>
<meta charset="utf-8">
<title>Parley Works – PowerPoint Template</title>
<link rel="stylesheet" href="https://fonts.googleapis.com/css2?family=Roboto+Condensed:wght@300;400;700&family=Roboto:wght@400;500;700&display=swap">
<style>
:root{
  --green:#8cc63f;
  --green-light:#bfe08a;
  --green-pale:#c9e4a0;
  --purple:#6a1bb0;
  --purple-mid:#8e58c8;
  --purple-light:#b598dc;
  --slide-bg:#f2f2f2;
  --ink:#333;
  --muted:#8a8a8a;
  --page:#ffffff;
}
*{margin:0;padding:0;box-sizing:border-box}
html,body{width:1200px;height:2194px;overflow:hidden;background:var(--page)}
body{position:relative;font-family:"Roboto",Arial,sans-serif;color:var(--ink)}

.sheet-header .brand{position:absolute;left:176px;top:160px;font:500 30px "Roboto",Arial,sans-serif;color:var(--green)}
.sheet-header .brand-mark{display:inline-block;width:16px;height:16px;background:var(--purple);margin-right:8px;vertical-align:2px}
.sheet-header .headline{position:absolute;left:421px;top:136px;font:400 54px "Roboto Condensed",Arial,sans-serif;letter-spacing:5px;color:var(--green)}
.sheet-header .headline b{font-weight:400;color:var(--purple)}

.slide{position:absolute;width:476px;height:268px;background:var(--slide-bg);overflow:hidden;box-shadow:8px 10px 22px rgba(0,0,0,.28)}
.col-a{left:88px}.col-b{left:624px}
.row-1{top:309px}.row-2{top:631px}.row-3{top:952px}.row-4{top:1274px}.row-5{top:1596px}

.abs{position:absolute}
.photo{position:absolute}
.logo{position:absolute;font:500 13px "Roboto",Arial,sans-serif;color:var(--green);white-space:nowrap}
.logo.right{right:34px;top:36px;font-size:11px}
.logo.white{color:#fff}
.slide-title{position:absolute;left:36px;top:24px;font:400 22px "Roboto",Arial,sans-serif;color:var(--green)}
.slide-sub{position:absolute;left:36px;top:53px;font-size:5px;color:var(--purple-mid)}
.footer{position:absolute;left:35px;bottom:7px;font-size:4.5px;color:var(--muted)}
.footer b{color:var(--green);font-weight:500}
.page-no{position:absolute;right:38px;bottom:7px;font-size:4.5px;color:var(--muted)}
.body-text{position:absolute;font-size:4.6px;line-height:1.55;color:#666;text-align:justify}
.body-text p+p{margin-top:6px}

.cover{background:linear-gradient(90deg,var(--green) 0%,#8a9ab0 50%,var(--purple) 100%)}
.cover-title{position:absolute;left:0;right:0;text-align:center;color:#fff;font-family:"Roboto Condensed",Arial,sans-serif;text-shadow:0 1px 3px rgba(0,0,0,.4)}
.cover-title .t{font-size:25px;line-height:1.1}
.cover-title .s{font-size:16px;font-weight:300}

.toc-item{position:absolute;width:120px}
.toc-num{display:inline-block;width:17px;height:18px;color:#fff;font:400 12px/18px "Roboto Condensed",Arial,sans-serif;text-align:center}
.toc-num.g{background:var(--green)}.toc-num.p{background:var(--purple)}
.toc-item h4{font:400 6.5px "Roboto",Arial,sans-serif;margin-top:6px;color:#222}
.toc-item p{font-size:4px;color:#aaa;line-height:1.5}
.toc-heading{position:absolute;left:31px;top:152px;font-family:"Roboto Condensed",Arial,sans-serif;line-height:.95}
.toc-heading .a{color:var(--purple);font-size:13px}
.toc-heading .b{color:var(--green);font-size:19px}

.callout{position:absolute;font:400 8.5px "Roboto",Arial,sans-serif;color:#222;line-height:1.05}
.callout small{display:block;font-size:5px;color:#444}
.callout.r{text-align:right}

.grid{position:absolute;left:44px;top:80px;display:grid;grid-template-columns:repeat(3,126px);grid-template-rows:repeat(2,74px);gap:1px}
.cell{padding:8px 9px;color:#fff}
.cell h5{font:400 8.5px "Roboto",Arial,sans-serif;margin-bottom:3px}
.cell h5::after{content:"";display:block;width:12px;height:1px;background:#fff;margin-top:3px}
.cell p{font-size:4.6px;line-height:1.6}
.c1{background:var(--green)}.c2{background:var(--purple)}.c3{background:var(--purple-mid)}
.c4{background:var(--green-light)}.c5{background:var(--green-pale)}.c6{background:var(--purple-light)}

.contact-box{position:absolute;left:43px;top:22px;width:192px;height:198px;background:var(--green)}
.contact-box h2{position:absolute;left:30px;top:28px;font:400 28px "Roboto Condensed",Arial,sans-serif;color:#fff;letter-spacing:1.5px}
.contact-line{position:absolute;left:40px;display:flex;align-items:center;gap:9px;font-size:6px;letter-spacing:1.4px;color:#fff}
</style>
</head>
<body>

<header class="sheet-header">
  <div class="brand"><span class="brand-mark"></span>Parley Works</div>
  <div class="headline">POWERPOINT <b>TEMPLATE</b></div>
</header>

<!-- Title slide A -->
<section class="slide cover col-a row-1">
  <div class="photo" role="img" aria-label="City skyline at dusk, tinted green and purple" style="left:41px;top:24px;width:396px;height:190px;background:linear-gradient(90deg,#5f7a4a 0%,#7d8a78 50%,#8d6fb5 100%)"></div>
  <svg class="abs" style="left:110px;top:210px" width="70" height="40"><polygon points="0,0 70,0 0,36" fill="#7a8c66"/></svg>
  <svg class="abs" style="left:300px;top:210px" width="70" height="40"><polygon points="0,0 70,0 70,36" fill="#7f6aa6"/></svg>
  <svg class="abs" style="left:250px;top:68px" width="90" height="100"><path d="M0 18 A34 34 0 1 1 0 82" fill="none" stroke="#7e7c90" stroke-width="12"/><circle cx="66" cy="50" r="3" fill="var(--green)"/></svg>
  <div class="logo white" style="left:58px;top:44px"><span style="display:inline-block;width:8px;height:8px;background:#fff;margin-right:4px"></span>Parley Works</div>
  <div class="cover-title" style="top:162px"><div class="t">Your title slide go here</div><div class="s">Your sub - title slide go here</div></div>
</section>

<!-- Title slide B -->
<section class="slide cover col-b row-1" style="background:linear-gradient(90deg,var(--green),#8a7fc0 60%,var(--purple))">
  <div class="photo" role="img" aria-label="City skyline under a blue sky" style="left:39px;top:8px;width:412px;height:230px;background:linear-gradient(180deg,#6faee6 0%,#8fb4e4 55%,#6a7fa8 100%)"></div>
  <svg class="abs" style="left:238px;top:8px" width="90" height="120"><path d="M6 0 V80 M14 0 V40 A34 34 0 1 1 14 92" fill="none" stroke="#7f8f92" stroke-width="10"/><circle cx="74" cy="66" r="3" fill="#fff"/></svg>
  <div class="logo white" style="left:52px;top:44px;font-size:11px"><span style="display:inline-block;width:7px;height:7px;background:#fff;margin-right:4px"></span>Parley Works</div>
  <div class="cover-title" style="top:192px"><div class="t">Your title slide go here</div><div class="s">Your sub - title slide go here</div></div>
  <div class="footer" style="left:52px"><b style="color:#fff">Parley Works</b> - Business Presentation</div>
</section>

<!-- Table of content -->
<section class="slide col-a row-2">
  <div class="logo" style="left:34px;top:62px"><span style="display:inline-block;width:8px;height:8px;background:var(--purple);margin-right:4px"></span>Parley Works</div>
  <div class="toc-heading"><div class="a">TABLE OF</div><div class="b">CONTENT</div></div>
  <div class="body-text" style="left:32px;top:188px;width:143px;font-size:4.4px">Use this page to list the main parts of the deck. Each entry below holds a short heading and a line of detail so the audience can follow the order of topics. Keep the wording brief and clear, and match the numbers to the section slides that follow in the presentation.</div>
  <div class="toc-item" style="left:199px;top:50px"><span class="toc-num g">1</span><h4>Opening and aims</h4><p>short line of detail for this part<br>of the deck goes here in brief</p></div>
  <div class="toc-item" style="left:335px;top:50px"><span class="toc-num p">2</span><h4>Market overview</h4><p>short line of detail for this part<br>of the deck goes here in brief</p></div>
  <div class="toc-item" style="left:200px;top:114px"><span class="toc-num g">3</span><h4>Our approach</h4><p>short line of detail for this part<br>of the deck goes here in brief</p></div>
  <div class="toc-item" style="left:336px;top:114px"><span class="toc-num p">4</span><h4>Key findings</h4><p>short line of detail for this part<br>of the deck goes here in brief</p></div>
  <div class="toc-item" style="left:201px;top:178px"><span class="toc-num g">5</span><h4>Action plan</h4><p>short line of detail for this part<br>of the deck goes here in brief</p></div>
  <div class="toc-item" style="left:337px;top:178px"><span class="toc-num p">6</span><h4>Next steps</h4><p>short line of detail for this part<br>of the deck goes here in brief</p></div>
  <div class="footer"><b>Parley Works</b> - Business Presentation</div><div class="page-no">Page:3</div>
</section>

<!-- Text slide -->
<section class="slide col-b row-2">
  <svg class="abs" style="left:96px;top:64px" width="310" height="180"><path d="M0 0H150V145H95L75 165V145H0Z" fill="#e6eedb"/><path d="M160 0H320V140H185V160L160 140Z" fill="#e5dced"/></svg>
  <div class="slide-title">Your title slide go here</div>
  <div class="slide-sub">A short line that introduces the topic of this slide in brief</div>
  <div class="logo right"><span style="display:inline-block;width:7px;height:7px;background:var(--purple);margin-right:3px"></span>Parley Works</div>
  <div class="body-text" style="left:32px;top:76px;width:414px">
    <p>This page holds a full block of text for a detailed point. Open with the main idea, then explain it in plain words so the reader can follow along. Add the facts that support the point, name the source where it helps, and note any limits of the data. Keep each line focused on one thought and avoid repeating the heading. Where a list would read better, break the paragraph into short parts and let the spacing do the work.</p>
    <p>The second paragraph builds on the first. Describe what the findings mean for the client, which options were weighed, and why one path was chosen over the others. Point to the risks and the steps that reduce them. Give a rough sense of time and cost so the reader can plan. Finish with a clear link to the next slide so the story of the deck keeps moving from one idea to the next without a gap.</p>
    <p>Use the last paragraph for a short summary. State the result in one or two lines, restate the key number, and close with the action you want the audience to take after the meeting has ended.</p>
  </div>
  <div class="footer"><b>Parley Works</b> - Business Presentation</div><div class="page-no">Page:4</div>
</section>

<!-- Image left slide -->
<section class="slide col-a row-3">
  <div class="slide-title">Your title slide go here</div>
  <div class="slide-sub">A short line that introduces the topic of this slide in brief</div>
  <div class="logo right"><span style="display:inline-block;width:7px;height:7px;background:var(--purple);margin-right:3px"></span>Parley Works</div>
  <svg class="abs" style="left:34px;top:70px" width="220" height="185">
    <path d="M0 0H146V47A28 28 0 1 0 146 103V145H54L54 178L30 145H0Z" fill="#9db7e0"/>
    <circle cx="175" cy="75" r="28" fill="#7fa3d8"/>
    <circle cx="152" cy="75" r="2" fill="#fff"/>
  </svg>
  <div class="photo" role="img" aria-label="City skyline at dusk" style="left:34px;top:70px;width:146px;height:145px;background:linear-gradient(180deg,#7fa5e0,#b7a6d2 60%,#6c7a92);clip-path:polygon(0 0,100% 0,100% 100%,0 100%)"></div>
  <div class="body-text" style="left:259px;top:76px;width:185px">
    <p>Place the main text for this slide here. Start with the core message and then add the detail that supports it. Keep the tone plain and direct so a busy reader can scan the block and still take in the point. Use short sentences where you can, and name any number that matters. The image on the left should echo the idea in the text and give the page a clear focus for the eye.</p>
    <p>A second block can add context or a short example from client work. Explain what changed, how it was measured and what came next. Close with one line that leads into the following slide.</p>
  </div>
  <div class="footer"><b>Parley Works</b> - Business Presentation</div><div class="page-no">Page:5</div>
</section>

<!-- Image right slide -->
<section class="slide col-b row-3">
  <div class="slide-title">Your title slide go here</div>
  <div class="slide-sub">A short line that introduces the topic of this slide in brief</div>
  <div class="logo right"><span style="display:inline-block;width:7px;height:7px;background:var(--purple);margin-right:3px"></span>Parley Works</div>
  <div class="body-text" style="left:37px;top:76px;width:240px">
    <p>Place the main text for this slide here. Start with the core message and then add the detail that supports it. Keep the tone plain and direct so a busy reader can scan the block and still take in the point. Use short sentences where you can, and name any number that matters. The image on the right should echo the idea in the text and give the page a clear focus for the eye of the reader.</p>
    <p>A second block can add context or a short example from client work. Explain what changed, how it was measured and what came next. Close with one line that leads into the following slide.</p>
  </div>
  <div class="photo" role="img" aria-label="City skyline at dusk" style="left:296px;top:72px;width:146px;height:152px;background:linear-gradient(180deg,#7fa5e0,#b7a6d2 60%,#6c7a92);clip-path:path('M0 0H146V152H88L70 180V152H0V104A30 30 0 1 0 0 44Z')"></div>
  <div class="footer"><b>Parley Works</b> - Business Presentation</div><div class="page-no">Page:6</div>
</section>

<!-- Puzzle infographic A -->
<section class="slide col-a row-4">
  <div class="slide-title">Puzzle infographic</div>
  <div class="slide-sub">A short line that explains what the chart below is showing</div>
  <div class="logo right"><span style="display:inline-block;width:7px;height:7px;background:var(--purple);margin-right:3px"></span>Parley Works</div>
  <svg class="abs" style="left:160px;top:68px" width="160" height="160">
    <g transform="translate(80 80) rotate(45)">
      <rect x="-50" y="-50" width="49" height="49" fill="var(--purple)"/>
      <rect x="1" y="-50" width="49" height="49" fill="var(--purple-mid)"/>
      <rect x="-50" y="1" width="49" height="49" fill="var(--green)"/>
      <rect x="1" y="1" width="49" height="49" fill="var(--green-light)"/>
      <circle cx="-25" cy="-52" r="9" fill="var(--purple)"/>
      <circle cx="52" cy="-25" r="9" fill="var(--purple-mid)"/>
      <circle cx="-52" cy="25" r="9" fill="var(--green)"/>
      <circle cx="25" cy="52" r="9" fill="var(--green-light)"/>
    </g>
    <g fill="#fff" font-family="Roboto,Arial,sans-serif" font-size="5.5" text-anchor="middle">
      <text x="80" y="44">Title</text><text x="80" y="50">here</text>
      <text x="44" y="80">Title</text><text x="44" y="86">here</text>
      <text x="116" y="80">Title</text><text x="116" y="86">here</text>
      <text x="80" y="116">Title</text><text x="80" y="122">here</text>
    </g>
  </svg>
  <svg class="abs" style="left:0;top:0" width="476" height="268"><g stroke="#b9b9d6" stroke-width=".6" stroke-dasharray="1.5 1.5"><line x1="276" y1="82" x2="348" y2="82"/><line x1="130" y1="123" x2="175" y2="123"/><line x1="300" y1="175" x2="348" y2="175"/></g></svg>
  <div class="callout" style="left:352px;top:74px">Lorem ipsum<small>Short note here</small></div>
  <div class="callout r" style="left:60px;top:111px;width:66px">Lorem ipsum<small>Short note here</small></div>
  <div class="callout" style="left:352px;top:168px">Lorem ipsum<small>Short note here</small></div>
  <div class="callout r" style="left:60px;top:203px;width:66px">Lorem ipsum<small>Short note here</small></div>
  <div class="footer"><b>Parley Works</b> - Business Presentation</div><div class="page-no">Page:7</div>
</section>

<!-- Puzzle infographic B -->
<section class="slide col-b row-4">
  <div class="slide-title">Puzzle infographic</div>
  <div class="slide-sub">A short line that explains what the chart below is showing</div>
  <div class="logo right"><span style="display:inline-block;width:7px;height:7px;background:var(--purple);margin-right:3px"></span>Parley Works</div>
  <svg class="abs" style="left:0;top:0" width="476" height="268">
    <g transform="translate(236 114) rotate(-40)"><rect x="-22" y="-22" width="44" height="44" fill="var(--green)"/><circle cx="0" cy="-24" r="8" fill="var(--green)"/><circle cx="24" cy="0" r="8" fill="var(--green)"/><circle cx="0" cy="0" r="8" fill="#fff"/><path d="M0 0V-8A8 8 0 0 1 8 0Z" fill="var(--green)"/></g>
    <g transform="translate(184 170) rotate(40)"><rect x="-22" y="-22" width="44" height="44" fill="var(--purple-mid)"/><circle cx="0" cy="-24" r="8" fill="var(--purple-mid)"/><circle cx="-24" cy="0" r="8" fill="var(--purple-mid)"/><rect x="-6" y="-5" width="12" height="9" fill="none" stroke="#fff" stroke-width="1.4"/></g>
    <g transform="translate(290 178) rotate(40)"><rect x="-22" y="-22" width="44" height="44" fill="var(--purple)"/><circle cx="0" cy="-24" r="8" fill="var(--purple)"/><circle cx="24" cy="0" r="8" fill="var(--purple)"/><path d="M-5 -7H5L-5 7H5Z" fill="#fff" transform="rotate(-40)"/></g>
    <g stroke="#9a9ac8" stroke-width=".6" stroke-dasharray="1.5 1.5"><line x1="262" y1="108" x2="322" y2="108"/><line x1="134" y1="175" x2="152" y2="175"/><line x1="320" y1="178" x2="342" y2="178"/></g>
  </svg>
  <div class="callout" style="left:330px;top:98px">Key Point<small>Short note for this point<br>goes here in brief</small></div>
  <div class="callout r" style="left:40px;top:166px;width:90px">Key Point<small>Short note for this point<br>goes here in brief</small></div>
  <div class="callout" style="left:352px;top:167px">Key Point<small>Short note for this point<br>goes here in brief</small></div>
  <div class="footer"><b>Parley Works</b> - Business Presentation</div><div class="page-no">Page:8</div>
</section>

<!-- Grid slide -->
<section class="slide col-a row-5">
  <div class="slide-title">Your title slide here</div>
  <div class="slide-sub">A short line that explains what the boxes below are showing</div>
  <div class="logo right"><span style="display:inline-block;width:7px;height:7px;background:var(--purple);margin-right:3px"></span>Parley Works</div>
  <div class="grid">
    <div class="cell c1"><h5>Title here</h5><p><b>Point one</b> is a short note on this part of the plan. Add detail here.</p></div>
    <div class="cell c2"><h5>Title here</h5><p><b>Point two</b> is a short note on this part of the plan. Add detail here.</p></div>
    <div class="cell c3"><h5>Title here</h5><p><b>Point three</b> is a short note on this part of the plan. Add detail here.</p></div>
    <div class="cell c4"><h5>Title here</h5><p><b>Point four</b> is a short note on this part of the plan. Add detail here.</p></div>
    <div class="cell c5"><h5>Title here</h5><p><b>Point five</b> is a short note on this part of the plan. Add detail here.</p></div>
    <div class="cell c6"><h5>Title here</h5><p><b>Point six</b> is a short note on this part of the plan. Add detail here.</p></div>
  </div>
  <div class="footer"><b>Parley Works</b> - Business Presentation</div><div class="page-no">Page:9</div>
</section>

<!-- Contact slide -->
<section class="slide col-b row-5" style="background:#6a4f9c">
  <div class="photo" role="img" aria-label="City skyline at night in purple tones" style="left:0;top:0;width:476px;height:268px;background:linear-gradient(180deg,#7659aa 0%,#6a4f9c 55%,#4d3a72 100%)"></div>
  <div class="photo" role="img" aria-label="Businessman on the phone holding a tablet" style="left:247px;top:22px;width:190px;height:205px;background:linear-gradient(135deg,#f2f2f2 0%,#d9dde6 45%,#2f3d63 100%)"></div>
  <svg class="abs" style="left:225px;top:70px" width="90" height="90"><circle cx="40" cy="40" r="36" fill="var(--purple-mid)"/><circle cx="10" cy="40" r="30" fill="var(--green)"/></svg>
  <svg class="abs" style="left:105px;top:218px" width="40" height="30"><polygon points="0,0 40,0 0,28" fill="var(--green)"/></svg>
  <svg class="abs" style="left:320px;top:210px" width="50" height="24"><polygon points="0,0 50,0 46,22" fill="#fff"/></svg>
  <div class="contact-box">
    <h2>Contact</h2>
    <div class="contact-line" style="top:112px"><svg width="14" height="12"><path d="M1 3L5 1L9 3L13 1V9L9 11L5 9L1 11Z" fill="none" stroke="#fff" stroke-width="1"/></svg>Parley St.No.1 NYC</div>
    <div class="contact-line" style="top:136px"><svg width="14" height="12"><rect x="1" y="2" width="12" height="9" fill="none" stroke="#fff" stroke-width="1"/><path d="M1 2L7 7L13 2" fill="none" stroke="#fff" stroke-width="1"/></svg>parleyworks@mail.com</div>
    <div class="contact-line" style="top:160px"><svg width="14" height="16"><rect x="3" y="1" width="8" height="14" rx="1" fill="none" stroke="#fff" stroke-width="1"/></svg>555-210-347</div>
  </div>
</section>

</body>
</html>
```